Postcard for dumpster rental business

We need an attractive post card to entice other businesses to use our dumpster rental service. This is a business to business situation.
Target Market(s)
Roofing, property restoration and remodeling contractors
Industry/Entity Type
Dumpster rentals
Font styles to use
Sans Serif
Colors
0054AA
0677BA
7BADD7
CADEEF
E8F1F8
Requirements
Must have
- tossbinhaul.com Dumpster rental Easy online booking Logo Guaranteed On Time Delivery (as a badge or button?) QR Code Picture of our dumpster (see website)
Nice to have
- Call to action "Order now!"

```html
<!DOCTYPE html>
<html lang="en">
<head>
<meta charset="utf-8">
<title>Tossbin Haul Postcard</title>
<link href="https://fonts.googleapis.com/css2?family=Montserrat:wght@400;500;600;700;800;900&display=swap" rel="stylesheet">
<style>
:root{
  --navy:#0f2a5c;
  --orange:#f36f21;
  --blue:#1565b0;
  --red:#e1141c;
  --paper:#ffffff;
  --mist:#eef1f7;
  --stage:#f3f0eb;
  --stamp:#dcdde0;
  --address:#f5f6f8;
  --ink:#1e2533;
}
*{margin:0;padding:0;box-sizing:border-box}
html,body{width:690px;height:1200px;overflow:hidden}
body{background:var(--stage);font-family:"Montserrat",sans-serif;position:relative;color:var(--ink)}
.card{position:absolute;left:35px;width:620px;height:440px;background:var(--paper);overflow:hidden;box-shadow:0 3px 8px rgba(0,0,0,.25)}
.card--front{top:132px}
.card--back{top:630px}
.abs{position:absolute}

/* front */
.top-band{left:0;top:0}
.brand{left:28px;top:14px;width:170px;color:#fff;text-align:center}
.brand__name{display:flex;align-items:center;justify-content:center;gap:6px;font-weight:800;font-size:19px;letter-spacing:.5px}
.brand__mark{width:12px;height:12px;background:#fff}
.brand__tag{font-weight:800;font-size:9px;letter-spacing:.6px;margin-top:3px;border-bottom:1px solid #fff;padding-bottom:2px}
.brand__phone{font-weight:600;font-size:7px;margin-top:2px}
.book-now{left:300px;top:14px;width:290px;text-align:right;color:#fff;font-weight:900;font-size:44px;letter-spacing:.5px;line-height:1}
.photo{left:0;top:74px}
.headline{left:42px;top:88px;color:var(--navy);font-weight:900;font-size:30px;line-height:30px;letter-spacing:-.2px}
.headline span{display:block}
.headline .dark{color:#22262e}
.intro{left:43px;top:190px;width:250px;font-size:10.5px;line-height:12.2px;font-weight:500;color:#1e1e1e}
.navy-band{left:0;top:254px;width:400px;height:48px;background:var(--navy)}
.order-badge{left:60px;top:244px}
.order-badge__text{left:65px;top:256px;width:195px;text-align:center;color:#fff;font-weight:700;line-height:22px}
.order-badge__text .l1{font-size:22px;display:block}
.order-badge__text .l2{font-size:26px;font-weight:800;display:block}
.feature{top:338px;display:flex;align-items:center;gap:6px;font-size:15px;line-height:19px;font-weight:500;color:#2a2a2a}
.feature em{font-style:normal;color:var(--orange)}
.feature--booking{left:40px}
.feature--delivery{left:168px}
.feature__text{text-align:center}
.bottom-band{left:0;top:384px}
.front-phone{left:26px;top:392px;display:flex;align-items:center;gap:8px;color:#fff;font-weight:600;font-size:29px}
.front-web{left:340px;top:398px;display:flex;align-items:center;gap:14px;color:#fff;font-weight:700;font-size:16.5px;line-height:24px}

/* back */
.back-panel{left:0;top:0;width:318px;height:440px}
.back-hero{left:0;top:0;width:318px;height:177px;background:var(--blue)}
.back-intro{left:29px;top:19px;width:280px;color:#fff;font-size:10.8px;line-height:12.8px;font-weight:500}
.bin-photo{left:31px;top:85px}
.order-tag{left:0;top:0}
.order-tag__text{left:212px;top:88px;width:112px;text-align:center;color:#fff;font-weight:600;font-size:21px;line-height:20px}
.take-all{left:0;top:177px;width:318px;height:56px;background:var(--mist)}
.take-all h2{position:absolute;left:28px;top:6px;color:var(--navy);font-weight:900;font-size:19px;line-height:22px}
.service-list{left:0;top:233px;width:318px;height:126px;background:var(--blue)}
.service-col{position:absolute;top:10px;list-style:none}
.service-col--a{left:28px}
.service-col--b{left:186px}
.service-col li{display:flex;gap:4px;color:#fff;font-weight:700;font-size:9.6px;line-height:10px;margin-bottom:4.5px}
.service-col li svg{flex:none;margin-top:1px}
.back-contact{left:0;top:359px;width:318px;height:81px;background:var(--orange)}
.back-phone{left:28px;top:10px;display:flex;align-items:center;gap:6px;color:#fff;font-weight:600;font-size:25px}
.back-web{left:30px;top:50px;display:flex;align-items:center;gap:10px;color:#fff;font-weight:700;font-size:13px}
.mail-brand{left:335px;top:30px;width:130px;text-align:center;color:var(--blue)}
.mail-brand .brand__name{font-size:15px;gap:5px}
.mail-brand .brand__mark{width:10px;height:10px;background:var(--blue)}
.mail-brand .brand__tag{font-size:7.5px;border-color:var(--blue)}
.mail-brand .brand__phone{font-size:6px}
.stamp{left:536px;top:22px;width:62px;height:61px;background:var(--stamp)}
.address-area{left:335px;top:200px;width:263px;height:155px;background:var(--address)}
</style>
</head>
<body>

<section class="card card--front">
  <svg class="abs top-band" width="620" height="74" viewBox="0 0 620 74">
    <polygon points="0,0 210,0 256,74 0,74" fill="var(--navy)"/>
    <polygon points="210,0 222,0 268,74 256,74" fill="#ffffff"/>
    <polygon points="222,0 620,0 620,74 268,74" fill="var(--orange)"/>
  </svg>
  <div class="abs brand">
    <div class="brand__name"><span class="brand__mark"></span>TOSSBIN HAUL</div>
    <div class="brand__tag">DUMPSTER RENTAL</div>
    <div class="brand__phone">(555) 014-2278</div>
  </div>
  <div class="abs book-now">BOOK NOW</div>

  <svg class="abs photo" width="620" height="310" viewBox="0 74 620 310" role="img" aria-label="Photo of a worker loading scrap into a large orange roll-off dumpster">
    <defs>
      <linearGradient id="photoTone" x1="0" y1="0" x2="0.3" y2="1">
        <stop offset="0" stop-color="#2a74c4"/>
        <stop offset="0.55" stop-color="#1c5aa6"/>
        <stop offset="0.62" stop-color="#e9781f"/>
        <stop offset="1" stop-color="#c75a12"/>
      </linearGradient>
    </defs>
    <circle cx="545" cy="250" r="225" fill="url(#photoTone)"/>
  </svg>

  <h1 class="abs headline"><span>DUMPSTER RENTAL</span><span>AND REMOVAL</span><span class="dark">SERVICES</span></h1>
  <p class="abs intro">Our competitive prices and high standards allow us to offer comprehensive, professional, and personalized customer-service to meet your practical and financial needs...</p>

  <div class="abs navy-band"></div>
  <svg class="abs order-badge" width="210" height="82" viewBox="60 244 210 82">
    <path d="M63,248 L262,248 L250,264 Q212,322 162,322 Q112,322 75,264 Z" fill="var(--red)"/>
  </svg>
  <div class="abs order-badge__text"><span class="l1">ORDER</span><span class="l2">NOW!</span></div>

  <div class="abs feature feature--booking">
    <svg width="24" height="32" viewBox="0 0 24 32"><rect x="2" y="2" width="14" height="24" rx="2" fill="none" stroke="#222" stroke-width="2"/><rect x="5" y="6" width="8" height="12" fill="#222"/><path d="M12,20 l4,-2 q2,0 2,2 l0,-4 q2,-1 3,1 l1,8 q0,6 -6,8 l-4,-4 z" fill="#222"/></svg>
    <div class="feature__text">Easy <em>online</em><br><em>booking</em></div>
  </div>
  <div class="abs feature feature--delivery">
    <svg width="48" height="24" viewBox="0 0 48 24"><rect x="2" y="4" width="20" height="13" fill="#222"/><path d="M22,8 h8 l5,5 v4 h-13 z" fill="#222"/><circle cx="9" cy="19" r="3.5" fill="#222" stroke="#fff"/><circle cx="28" cy="19" r="3.5" fill="#222" stroke="#fff"/><circle cx="42" cy="12" r="5" fill="none" stroke="#222" stroke-width="1.6"/><path d="M39.5,12 l2,2 l3,-4" fill="none" stroke="#222" stroke-width="1.6"/></svg>
    <div class="feature__text">Guaranteed <em>On</em><br><em>Time Delivery</em></div>
  </div>

  <svg class="abs bottom-band" width="620" height="56" viewBox="0 0 620 56">
    <polygon points="0,0 290,0 305,28 290,56 0,56" fill="var(--orange)"/>
    <polygon points="290,0 298,0 313,28 298,56 290,56 305,28" fill="#ffffff"/>
    <polygon points="298,0 620,0 620,56 298,56 313,28" fill="var(--navy)"/>
  </svg>
  <div class="abs front-phone">
    <svg width="24" height="24" viewBox="0 0 24 24"><path d="M6,3 l4,4 -2,3 q2,4 6,6 l3,-2 4,4 -3,3 q-9,0 -15,-10 z" fill="#fff"/><path d="M14,4 q5,1 6,6 M14,8 q2,0 2,2" fill="none" stroke="#fff" stroke-width="1.6"/></svg>
    (555) 014-2278
  </div>
  <div class="abs front-web">
    <svg width="20" height="20" viewBox="0 0 20 20"><circle cx="10" cy="10" r="8.5" fill="none" stroke="#fff" stroke-width="2"/><path d="M5,6 q4,1 3,5 q3,1 2,6 M12,3 q-1,3 3,4 q2,0 3,2" fill="none" stroke="#fff" stroke-width="2"/></svg>
    tossbinhaul.com
  </div>
</section>

<section class="card card--back">
  <div class="abs back-hero"></div>
  <p class="abs back-intro">Our competitive prices and high standards allow u to offer comprehensive, professional, and personalized customer-service to meet your practical and financial needs...</p>
  <svg class="abs bin-photo" width="248" height="92" viewBox="0 0 248 92" role="img" aria-label="Photo of an orange roll-off dumpster">
    <defs>
      <linearGradient id="binTone" x1="0" y1="0" x2="1" y2="1">
        <stop offset="0" stop-color="#f7902e"/>
        <stop offset="1" stop-color="#d9631a"/>
      </linearGradient>
    </defs>
    <rect x="0" y="0" width="248" height="92" fill="url(#binTone)"/>
  </svg>
  <svg class="abs order-tag" width="330" height="160" viewBox="0 0 330 160">
    <polygon points="324,79 214,79 187,113 214,147 324,147" fill="var(--red)"/>
    <polygon points="320,83 216,83 192,113 216,143 320,143" fill="none" stroke="#fff" stroke-width="1"/>
  </svg>
  <div class="abs order-tag__text">ORDER<br>NOW</div>

  <div class="abs take-all"><h2>WE TAKE JUST ABOUT<br>EVERYTHING</h2></div>

  <div class="abs service-list">
    <ul class="service-col service-col--a">
      <li><svg width="8" height="8" viewBox="0 0 8 8"><circle cx="4" cy="4" r="3.3" fill="none" stroke="#fff"/><path d="M2.4,4 l1.2,1.2 2-2.2" fill="none" stroke="#fff"/></svg>Refrigerator Disposal</li>
      <li><svg width="8" height="8" viewBox="0 0 8 8"><circle cx="4" cy="4" r="3.3" fill="none" stroke="#fff"/><path d="M2.4,4 l1.2,1.2 2-2.2" fill="none" stroke="#fff"/></svg>Garbage Removal</li>
      <li><svg width="8" height="8" viewBox="0 0 8 8"><circle cx="4" cy="4" r="3.3" fill="none" stroke="#fff"/><path d="M2.4,4 l1.2,1.2 2-2.2" fill="none" stroke="#fff"/></svg>Mattress Disposal</li>
      <li><svg width="8" height="8" viewBox="0 0 8 8"><circle cx="4" cy="4" r="3.3" fill="none" stroke="#fff"/><path d="M2.4,4 l1.2,1.2 2-2.2" fill="none" stroke="#fff"/></svg>Foreclosure Clean Outs</li>
      <li><svg width="8" height="8" viewBox="0 0 8 8"><circle cx="4" cy="4" r="3.3" fill="none" stroke="#fff"/><path d="M2.4,4 l1.2,1.2 2-2.2" fill="none" stroke="#fff"/></svg>Construction Waste<br>Removal</li>
      <li><svg width="8" height="8" viewBox="0 0 8 8"><circle cx="4" cy="4" r="3.3" fill="none" stroke="#fff"/><path d="M2.4,4 l1.2,1.2 2-2.2" fill="none" stroke="#fff"/></svg>Yard Waste Removal</li>
    </ul>
    <ul class="service-col service-col--b">
      <li><svg width="8" height="8" viewBox="0 0 8 8"><circle cx="4" cy="4" r="3.3" fill="none" stroke="#fff"/><path d="M2.4,4 l1.2,1.2 2-2.2" fill="none" stroke="#fff"/></svg>Trash Removal</li>
      <li><svg width="8" height="8" viewBox="0 0 8 8"><circle cx="4" cy="4" r="3.3" fill="none" stroke="#fff"/><path d="M2.4,4 l1.2,1.2 2-2.2" fill="none" stroke="#fff"/></svg>Appliance Removal</li>
      <li><svg width="8" height="8" viewBox="0 0 8 8"><circle cx="4" cy="4" r="3.3" fill="none" stroke="#fff"/><path d="M2.4,4 l1.2,1.2 2-2.2" fill="none" stroke="#fff"/></svg>Television Disposal<br>and Recycling</li>
      <li><svg width="8" height="8" viewBox="0 0 8 8"><circle cx="4" cy="4" r="3.3" fill="none" stroke="#fff"/><path d="M2.4,4 l1.2,1.2 2-2.2" fill="none" stroke="#fff"/></svg>Furniture Removal</li>
      <li><svg width="8" height="8" viewBox="0 0 8 8"><circle cx="4" cy="4" r="3.3" fill="none" stroke="#fff"/><path d="M2.4,4 l1.2,1.2 2-2.2" fill="none" stroke="#fff"/></svg>E-Waste Disposal</li>
      <li><svg width="8" height="8" viewBox="0 0 8 8"><circle cx="4" cy="4" r="3.3" fill="none" stroke="#fff"/><path d="M2.4,4 l1.2,1.2 2-2.2" fill="none" stroke="#fff"/></svg>Hot Tub Disposal</li>
    </ul>
  </div>

  <div class="abs back-contact">
    <div class="abs back-phone">
      <svg width="20" height="20" viewBox="0 0 24 24"><path d="M6,3 l4,4 -2,3 q2,4 6,6 l3,-2 4,4 -3,3 q-9,0 -15,-10 z" fill="#fff"/><path d="M14,4 q5,1 6,6 M14,8 q2,0 2,2" fill="none" stroke="#fff" stroke-width="1.6"/></svg>
      (555) 014-2278
    </div>
    <div class="abs back-web">
      <svg width="16" height="16" viewBox="0 0 20 20"><circle cx="10" cy="10" r="8.5" fill="none" stroke="#fff" stroke-width="2"/><path d="M5,6 q4,1 3,5 q3,1 2,6 M12,3 q-1,3 3,4 q2,0 3,2" fill="none" stroke="#fff" stroke-width="2"/></svg>
      tossbinhaul.com
    </div>
  </div>

  <div class="abs brand mail-brand">
    <div class="brand__name"><span class="brand__mark"></span>TOSSBIN HAUL</div>
    <div class="brand__tag">DUMPSTER RENTAL</div>
    <div class="brand__phone">(555) 014-2278</div>
  </div>
  <div class="abs stamp"></div>
  <div class="abs address-area"></div>
</section>

</body>
</html>
```